PowerPoint Design Project for Retirement Planning Company

Please design a powerpoint presentation template for our retirement planning company called Pine Harbor Advisors. We need a cover page and slide pages in both portrait and landscape orientation. We make many presentations to clients.

Our tagline is "Retirement Planning. Simplified." We are educators in the retirement planning space. Our company educates small and mid-sized businesses in the board room and break room on how to select a retirement plan for the company and their employees that will help them retire ready. Our slide deck needs to have appeal to a CEO in the board room and a blue collar worker in the breakroom.

We are looking for a template that incorporates our logo, tagline images, colors - green, gray and brown (see uploaded files for examples). The design needs to be clean with plenty of space for text. It needs to be crisp, modern, and eye catching.

We look forward to seeing how you use the images in our business card and logo to achieve a pleasing design. You are the experts so we hope you will develop some innovative designs that wow us and give our clients the confidence that we are experts and put together.
Updates

Designers - Thanks for your great work so far.  

Please do not include the website address on the powerpoint template.

Please provide one template per submission.  When they are grouped together, it is too hard to see the details on your slides.  

Thanks!

Target Market(s)

CEOs and Executive teams at small to medium sized businesses that care about their employees future retirement

Industry/Entity Type

Landscape

Requirements
Must have
• 1) Cover Page (should double as a report cover as well)

2) Second Page for text

3) Third Page for illustrations/graphs/charts

Landscape orientation and Portrait orientation

Colors:

Brown light : C=35, M=60, Y=80, K=25
Brown dark : C=40, M=70, Y=100, K=50

Gray Icon Border: C=0, M=0, Y=0, K=80
Gray Icon Background: C=0, M=0, Y=0, K=5
Gray Letters: C=0, M=0, Y=0, K=80
Gray Light Person: C=0, M=0, Y=0, K=40
Gray Dark Person: C=0, M=0, Y=0, K=60
Gray Dark Wheel Checked: C=0, M=0, Y=0, K=90

Green Light 1: C=40, M=8, Y=85, K=0
Green Light 2: C=53, M=17, Y=100, K=0
Green Dark: C=67, M=39, Y=100, K=27

White: C=0, M=0, Y=0, K=0

Black: C=0, M=0, Y=0, K=100

Fonts:
Logo and graphics files
Footlight MT Light
BrowalliaUPC

Business card/Letterhead files
Calisto MT
Segoe UI

Nice to have
• Please look at the back of our business card design. It has a version of our logo in an abstract form. Consider this concept in full color or a grayed out version as a backdrop.

Use of the "hill" with our tagline is another concept that could be incorporated into the design. See front of our business card and letterhead.

I have uploaded a diagram (wheel diagram full color) that we use to describe our services, plus all the images we use to describe our services (pdf). These images needs to look good as content on a slide.

```html
<!DOCTYPE html>
<html lang="en">
<head>
<meta charset="utf-8">
<title>Pine Harbor Advisors – Slide Template</title>
<link rel="stylesheet" href="https://fonts.googleapis.com/css2?family=Roboto+Condensed:wght@400;700&family=Saira+Semi+Condensed:wght@600&family=Crimson+Text&family=Open+Sans:wght@700&display=swap">
<style>
  :root {
    --green-dark: #3f5a1f;
    --green-mid: #5b7a2c;
    --green-light: #8db63f;
    --green-text: #3d5218;
    --gray-text: #666666;
    --gray-frame: #3a3a3a;
    --gray-bg: #f1f1f1;
    --brown: #8b5e3c;
    --white: #ffffff;
  }
  html, body {
    margin: 0;
    padding: 0;
    width: 1200px;
    height: 900px;
    overflow: hidden;
    background: var(--white);
  }
  .slide {
    position: relative;
    width: 1200px;
    height: 900px;
    overflow: hidden;
    background: var(--white);
    font-family: "Roboto Condensed", sans-serif;
  }
  .header {
    position: absolute;
    left: 0; top: 0;
    width: 1200px; height: 102px;
    background: linear-gradient(90deg, #2f4514 0%, var(--green-mid) 35%, #6f8d3c 60%, var(--green-mid) 85%, #3e5a1d 100%);
  }
  .brand {
    position: absolute;
    left: 0; top: 0;
    width: 375px; height: 102px;
    background: var(--white);
    display: flex;
    align-items: center;
    gap: 14px;
    padding-left: 42px;
    box-sizing: border-box;
  }
  .brand-mark {
    width: 46px; height: 46px;
    border-radius: 50%;
    background: var(--green-dark);
    flex: none;
  }
  .brand-name {
    font-family: "Roboto Condensed", sans-serif;
    font-weight: 700;
    font-size: 31px;
    color: var(--green-dark);
    white-space: nowrap;
  }
  .presentation-title {
    position: absolute;
    right: 30px; top: 18px;
    margin: 0;
    font-family: "Roboto Condensed", sans-serif;
    font-weight: 400;
    font-size: 52px;
    line-height: 1;
    color: var(--white);
  }
  .subtitle-band {
    position: absolute;
    left: 0; top: 102px;
    width: 1200px; height: 168px;
    background: linear-gradient(180deg, #ffffff 0%, #ffffff 58%, #ececec 62%, #ffffff 100%);
  }
  .subtitle {
    position: absolute;
    left: 36px; top: 150px;
    margin: 0;
    font-family: "Saira Semi Condensed", sans-serif;
    font-weight: 600;
    font-size: 46px;
    line-height: 1;
    letter-spacing: 1px;
    color: var(--green-text);
  }
  .points {
    position: absolute;
    left: 36px; top: 318px;
    margin: 0; padding: 0;
    list-style: none;
  }
  .points li {
    display: flex;
    align-items: center;
    height: 69px;
    font-size: 25px;
    color: var(--gray-text);
  }
  .points svg {
    width: 14px; height: 16px;
    margin-right: 16px;
    flex: none;
  }
  .feature {
    position: absolute;
    left: 757px; top: 385px;
    width: 386px; height: 293px;
    box-sizing: border-box;
    border: 6px solid var(--gray-frame);
    border-radius: 14px;
    background: var(--white);
    padding: 10px;
    box-shadow: 0 2px 6px rgba(0,0,0,0.25);
  }
  .feature-art {
    width: 100%; height: 100%;
    border-radius: 6px;
    background: radial-gradient(ellipse at 55% 55%, #8b5e3c 0%, #a8a8a8 55%, #ececec 100%);
  }
  .feature-caption {
    position: absolute;
    left: 757px; top: 688px;
    width: 386px;
    text-align: center;
    font-family: "Crimson Text", serif;
    font-size: 36px;
    color: #444444;
  }
  .footer {
    position: absolute;
    left: 0; top: 845px;
    width: 1200px; height: 55px;
    background: linear-gradient(90deg, #2f4514 0%, var(--green-mid) 40%, #6f8d3c 65%, #3e5a1d 100%);
    display: flex;
    align-items: center;
    justify-content: space-between;
    padding: 0 18px 0 22px;
    box-sizing: border-box;
    font-family: "Open Sans", sans-serif;
    font-weight: 700;
    font-size: 24px;
    color: var(--white);
  }
  .page-number { font-size: 27px; }
</style>
</head>
<body>
<main class="slide">
  <header class="header">
    <div class="brand">
      <span class="brand-mark"></span>
      <span class="brand-name">Pine Harbor Advisors</span>
    </div>
    <h1 class="presentation-title">Presentation Title here</h1>
  </header>

  <div class="subtitle-band"></div>
  <h2 class="subtitle">Sub Title here</h2>

  <ul class="points">
    <li><svg viewBox="0 0 14 16"><path d="M3 2 L10 8 L3 14" fill="none" stroke="#6f9a2a" stroke-width="3.5"/></svg>Lorem ipsum dolor sit ipusm Lorem ipsum dolor sit ipusm</li>
    <li><svg viewBox="0 0 14 16"><path d="M3 2 L10 8 L3 14" fill="none" stroke="#6f9a2a" stroke-width="3.5"/></svg>Lorem ipsum dolor sit ipusm Lorem ipsum</li>
    <li><svg viewBox="0 0 14 16"><path d="M3 2 L10 8 L3 14" fill="none" stroke="#6f9a2a" stroke-width="3.5"/></svg>Lorem ipsum dolor sit ipusm Lorem ipsum</li>
    <li><svg viewBox="0 0 14 16"><path d="M3 2 L10 8 L3 14" fill="none" stroke="#6f9a2a" stroke-width="3.5"/></svg>Lorem ipsum dolor sit ipusm Lorem ipsum</li>
    <li><svg viewBox="0 0 14 16"><path d="M3 2 L10 8 L3 14" fill="none" stroke="#6f9a2a" stroke-width="3.5"/></svg>Lorem ipsum dolor sit ipusm Lorem ipsum dolor sit ipusm</li>
    <li><svg viewBox="0 0 14 16"><path d="M3 2 L10 8 L3 14" fill="none" stroke="#6f9a2a" stroke-width="3.5"/></svg>Lorem ipsum dolor sit ipusm Lorem ipsum dolor sit ipusm</li>
    <li><svg viewBox="0 0 14 16"><path d="M3 2 L10 8 L3 14" fill="none" stroke="#6f9a2a" stroke-width="3.5"/></svg>Lorem ipsum dolor sit ipusm Lorem ipsum dolor sit ipusm</li>
  </ul>

  <figure class="feature" style="margin:0">
    <div class="feature-art" role="img" aria-label="Icon of a board meeting: figures seated around a brown table with a chart document"></div>
  </figure>
  <div class="feature-caption">BoardRoom</div>

  <footer class="footer">
    <span class="tagline">Retirement Plans. Simplified.</span>
    <span class="page-number">Page No. 01</span>
  </footer>
</main>
</body>
</html>
```